New Signage Design Project

Real estate company looking for signage, PowerPoint and stationery branding. Signs will be placed in front of homes and other properties being sold

Name of company is Birch Crest, LLC

Requirements
Must have
• Name of company - Birch Crest, LLC

```html
<!DOCTYPE html>
<html lang="en">
<head>
<meta charset="UTF-8">
<title>Birch Crest, LLC – For Sale Sign</title>
<link rel="stylesheet" href="https://fonts.googleapis.com/css2?family=Roboto+Condensed:wght@700&display=swap">
<style>
  :root {
    --red: #e3202a;
    --red-deep: #b5161d;
    --red-dark: #8e0f14;
    --ink: #111111;
    --white: #ffffff;
    --gold-light: #ffd84a;
    --gold-mid: #f5b31f;
    --gold-deep: #d98a12;
    --photo-warm: #f3dcc8;
    --photo-soft: #faeee4;
  }
  html, body {
    margin: 0;
    padding: 0;
    width: 1200px;
    height: 800px;
    overflow: hidden;
    background: var(--white);
  }
  .sign {
    position: relative;
    width: 1200px;
    height: 800px;
    overflow: hidden;
    background: var(--white);
    font-family: "Roboto Condensed", "Arial Narrow", sans-serif;
    font-weight: 700;
  }
  .top-band {
    position: absolute;
    left: 0; top: 0;
    width: 1200px; height: 114px;
    background: linear-gradient(180deg, var(--red) 0%, var(--red-deep) 100%);
  }
  .hero-photo {
    position: absolute;
    left: 636px; top: 114px;
    width: 564px; height: 446px;
    background: linear-gradient(90deg, var(--white) 0%, var(--photo-soft) 35%, var(--photo-warm) 100%);
  }
  .headline {
    position: absolute;
    margin: 0;
    line-height: 1;
    text-transform: uppercase;
  }
  .headline-lead {
    left: 32px;
    top: 190px;
    font-size: 84px;
    letter-spacing: -1.5px;
    color: var(--ink);
  }
  .headline-main {
    left: 26px;
    top: 282px;
    font-size: 222px;
    letter-spacing: 0;
    color: var(--red);
  }
  .bottom-band {
    position: absolute;
    left: 0; top: 560px;
    width: 1200px; height: 240px;
    background: linear-gradient(180deg, var(--red) 0%, var(--red-deep) 60%, var(--red-dark) 100%);
  }
  .company-name {
    position: absolute;
    left: 40px; top: 738px;
    width: 270px;
    text-align: center;
    font-size: 32px;
    line-height: 1;
    color: var(--white);
    text-transform: uppercase;
  }
  .divider {
    position: absolute;
    left: 350px; top: 594px;
    width: 2px; height: 174px;
    background: var(--red-dark);
  }
  .contact-label {
    position: absolute;
    left: 410px; top: 593px;
    margin: 0;
    font-size: 56px;
    line-height: 1;
    color: var(--white);
    text-transform: uppercase;
  }
  .contact-phone {
    position: absolute;
    left: 406px; top: 652px;
    margin: 0;
    font-size: 122px;
    line-height: 1;
    letter-spacing: 8px;
    white-space: nowrap;
    background: linear-gradient(180deg, var(--gold-light) 0%, var(--gold-mid) 50%, var(--gold-deep) 100%);
    -webkit-background-clip: text;
    background-clip: text;
    color: transparent;
  }
</style>
</head>
<body>
  <div class="sign">
    <div class="top-band"></div>
    <div class="hero-photo" role="img" aria-label="Photo of one hand handing a house key on a house-shaped keyring into another open hand"></div>
    <h1 class="headline headline-lead">This property is</h1>
    <p class="headline headline-main">For sale</p>
    <div class="bottom-band"></div>
    <div class="company-name">Birch Crest, LLC</div>
    <div class="divider"></div>
    <p class="contact-label">Contact:</p>
    <p class="contact-phone">555 246 810</p>
  </div>
</body>
</html>
```